Blog design for health, nutrition and exercise blogging (fernwellnotes.com)

FernwellNotes.com will be run by an exercise and nutritional scientist and aims to provide educational evidence-based articles on a variety of topics related to nutrition, exercise, sports, nutritional supplements and health.

The articles will cover topics like:
• Translating science into layman’s terms
• Age-specific nutritional advice
• Interpreting food and supplement labels properly
• Demystifying nutritional supplements
• Supplements and nutrition for sports and exercise performance

Target Market(s)

The target audience is the mainstream public across all age groups and is not necessarily restricted to sports persons.

Industry/Entity Type

Health And Wellness

Coding

Coded - Design and coding required

Number of Pages Required

5+ page

Font styles to use
Sans Serif

Requirements
Must have
• • About FernwellNotes.com and its mission
• • About author-highlighting background, publications and achievements
• • Easily accessible website sections
• • Easy article categorization (see below)
• • Clear navigation
• • Easy to manage website (frequent article/ blog updates)
• • Easy links to social media pages (Facebook/ twitter/ etc.)
• • Easy to share articles
• • Mobile and tablet friendly
• • Contact and feedback submission form
• • Community section to build a forum and following
• Article categorization
• The following tabs need to be present to categorize the articles
• A. Nutrition, with the subsections below:
• Proteins/ amino acids
• Carbohydrates
• Fats
• Herbals and Nutraceuticals
• Vitamins and minerals
• B. Exercise and Sports
• C. Age-specific: children, teen, adults, seniors (may contain articles from other categories)
• D. Condition-specific: e.g. obesity, ageing, diabetes, Alzheimer’s, etc. (may contain articles from other categories)
• Website logo-depicting science and health/ fitness
• Health/ Fitness/ Lifestyle/ Science (DNA strands, etc.)/
• Bodybuilding Images
• images of active and exercising kids, young adults and elderly
• Images of herbs to depict preference for natural alternatives with regard to nutrition and supplementation
• Images of supplement containers-protein powders/ capsules/ gel capsules etc.

```html
<!DOCTYPE html>
<html lang="en">
<head>
<meta charset="utf-8">
<title>FernwellNotes.com – Nutrition, Exercise &amp; Health</title>
<link rel="stylesheet" href="https://fonts.googleapis.com/css2?family=Open+Sans:wght@300;400;600;700&display=swap">
<style>
:root{
  --green:#3daa2e;
  --green-dark:#2f8c22;
  --blue:#1ba1dd;
  --blue-dark:#1386bb;
  --ink:#333;
  --muted:#777;
  --light:#f1f1f1;
  --panel:#e4e4e4;
  --footer:#1f1f1f;
  --footer-deep:#141414;
  --hero-top:#d5dcdf;
  --hero-bottom:#eef1f2;
  --white:#fff;
}
*{box-sizing:border-box;margin:0;padding:0}
html,body{width:1200px;height:3508px;overflow:hidden}
body{font-family:"Open Sans",Arial,sans-serif;color:var(--ink);background:var(--white);position:relative;font-size:13px;line-height:1.55}
.abs{position:absolute}

/* hero */
.hero{left:0;top:0;width:1200px;height:800px;background:linear-gradient(180deg,var(--hero-top),var(--hero-bottom))}
.nav{left:0;top:48px;width:1200px;height:40px;background:var(--green)}
.nav ul{list-style:none;display:flex;position:absolute;top:0;height:40px;align-items:center}
.nav li{color:var(--white);font-size:12px;font-weight:600;text-transform:uppercase;padding:0 16px;height:40px;line-height:40px}
.nav li.active{background:var(--green-dark)}
.nav .left{left:90px}
.nav .right{left:700px}
.topbar{left:960px;top:14px;font-size:11px;color:var(--muted);display:flex;gap:14px}
.topbar span:first-child{color:#d33;font-weight:600}
.logo{left:540px;top:10px;width:120px;height:100px;background:var(--white);box-shadow:0 2px 6px rgba(0,0,0,.2);display:flex;flex-direction:column;align-items:center;justify-content:center;gap:6px}
.logo i{display:block;width:34px;height:34px;border-radius:50%;background:var(--green)}
.logo b{font-size:12px;font-weight:700;color:var(--green)}
.dots{left:560px;top:740px;display:flex;gap:8px}
.dots i{width:9px;height:9px;border-radius:50%;background:rgba(255,255,255,.8)}
.dots i.on{background:var(--blue)}

/* feature cards */
.card{top:620px;width:318px;height:360px;background:var(--white);box-shadow:0 2px 8px rgba(0,0,0,.15)}
.card .photo{height:240px}
.card .cap{height:120px;background:var(--blue);color:var(--white);padding:18px 18px}
.card h3{font-size:14px;font-weight:700;text-transform:uppercase;margin-bottom:6px}
.card p{font-size:12px;opacity:.9}

/* welcome */
.author-photo{left:100px;top:1080px;width:300px;height:420px;background:linear-gradient(180deg,#e9e9e9,#cfcfcf 60%,#2c2c34 60%,#1e1e24)}
.welcome{left:440px;top:1080px;width:660px}
.welcome h2{font-size:30px;font-weight:300;text-transform:uppercase;color:#444;margin-bottom:8px}
.welcome h2 em{font-style:normal;color:var(--blue)}
.welcome h4{font-size:14px;font-weight:700;text-transform:uppercase}
.welcome h4 small{font-weight:400;text-transform:none;color:var(--muted);font-size:12px}
.welcome h5{font-size:16px;font-weight:600;margin-top:16px}
.welcome .lead{color:var(--blue);font-size:13px;margin-bottom:10px}
.welcome p{font-size:12px;color:var(--muted);margin-bottom:10px}
.btn{display:inline-block;background:var(--blue);color:var(--white);font-size:11px;font-weight:700;text-transform:uppercase;padding:7px 16px}

/* blog */
.section-title{left:0;top:1570px;width:1200px;text-align:center;font-size:34px;font-weight:300;text-transform:uppercase;color:#444}
.section-title:after{content:"";display:block;width:60px;height:3px;background:var(--blue);margin:10px auto 0}
.post{width:460px}
.post h3{font-size:16px;font-weight:600;text-transform:uppercase;color:#444}
.post .meta{font-size:11px;color:var(--muted);margin:4px 0 14px;border-bottom:1px solid #ddd;padding-bottom:8px}
.post .meta b{color:var(--blue);font-weight:400}
.post p{font-size:12px;color:var(--muted);margin-bottom:12px}
.post .foot{font-size:11px;color:var(--muted);display:flex;gap:22px;margin-top:14px}
.post .foot span:before{content:"";display:inline-block;width:9px;height:9px;border-radius:50%;background:var(--blue);margin-right:5px;vertical-align:-1px}
.catbar{height:50px;display:flex;align-items:center;gap:22px;padding:0 24px;color:var(--white);font-size:12px;font-weight:600}
.catbar span{display:flex;align-items:center;gap:8px}
.catbar span i{width:26px;height:26px;border-radius:50%;border:2px solid var(--white);display:block}

/* social panels */
.panels{left:0;top:2510px;width:1200px;height:440px;background:var(--panel)}
.panel{top:2540px;width:318px;height:380px;background:var(--white)}
.panel h3{height:44px;line-height:44px;padding-left:16px;font-size:14px;font-weight:700;text-transform:uppercase;color:#444;border-bottom:3px solid var(--blue);display:flex;align-items:center;gap:10px}
.panel h3 i{width:20px;height:20px;background:var(--blue);display:block}
.feed{list-style:none;padding:14px 16px}
.feed li{display:flex;gap:12px;margin-bottom:18px}
.feed .avatar{width:56px;height:56px;background:linear-gradient(135deg,#c9a98a,#8a6a55);flex:none}
.feed b{display:block;font-size:12px;color:var(--blue);font-weight:600}
.feed b small{color:var(--muted);font-weight:400;margin-left:6px}
.feed p{font-size:11px;color:var(--muted);line-height:1.4}
.testimonial{padding:18px 16px}
.testimonial .who{display:flex;gap:14px;align-items:center;margin-bottom:14px}
.testimonial .who .avatar{width:70px;height:70px;border-radius:50%;background:linear-gradient(135deg,#d6d6d6,#555);flex:none}
.testimonial .who b{display:block;color:var(--blue);font-size:13px}
.testimonial .who small{display:block;font-size:11px;color:var(--muted)}
.testimonial p{font-size:11px;color:var(--muted);border-left:3px solid var(--blue);padding-left:10px}
.testimonial .arrows{display:flex;gap:4px;margin-top:14px}
.testimonial .arrows i{width:22px;height:22px;background:#999;display:block}

/* footer */
.footer{left:0;top:2960px;width:1200px;height:130px;background:var(--footer)}
.footer input{position:absolute;left:100px;top:48px;width:270px;height:30px;border:0;padding:0 10px;font-family:inherit;font-size:12px}
.footer .btn{position:absolute;left:396px;top:48px;height:30px;line-height:16px}
.social{position:absolute;left:880px;top:52px;display:flex;gap:10px}
.social i{width:22px;height:22px;border-radius:50%;background:var(--blue);display:block}
.copy{left:0;top:3090px;width:1200px;height:34px;background:var(--footer-deep);color:#888;font-size:11px;line-height:34px}
.copy span{position:absolute}
.copy .l{left:100px}.copy .r{left:880px}
</style>
</head>
<body>

<div class="abs hero" role="img" aria-label="Close-up of colourful vitamin and mineral capsules"></div>
<div class="abs topbar"><span>Login</span><span>Register</span></div>
<nav class="abs nav">
  <ul class="left"><li class="active">Home</li><li>About Us</li><li>Blog</li></ul>
  <ul class="right"><li>Community</li><li>Subscribe</li><li>Contact Us</li></ul>
</nav>
<div class="abs logo"><i></i><b>FernwellNotes</b></div>
<div class="abs dots"><i class="on"></i><i></i><i></i><i></i></div>

<article class="abs card" style="left:100px">
  <div class="photo" role="img" aria-label="Fresh vegetables and measuring tape on a table" style="background:linear-gradient(135deg,#9dc46a,#e9efe0)"></div>
  <div class="cap"><h3>Nutrition &amp; Supplements</h3><p>Clear guides on food, labels and supplements made simple.</p></div>
</article>
<article class="abs card" style="left:441px">
  <div class="photo" role="img" aria-label="Woman stretching outdoors on a sunny lawn" style="background:linear-gradient(135deg,#6fae48,#d9e8b0)"></div>
  <div class="cap"><h3>Exercise &amp; Sports</h3><p>Training tips backed by research for every level.</p></div>
</article>
<article class="abs card" style="left:782px">
  <div class="photo" role="img" aria-label="Smiling family of three generations at home" style="background:linear-gradient(135deg,#c8a584,#efe4d6)"></div>
  <div class="cap"><h3>Family Health</h3><p>Advice for children, teens, adults and seniors alike.</p></div>
</article>

<div class="abs author-photo" role="img" aria-label="Portrait of the author in a dark suit and glasses"></div>
<section class="abs welcome">
  <h2>Welcome to <em>Nutrition</em></h2>
  <h4>Mr. Daniel Harrow <small>President, Nutrition Exercise</small></h4>
  <h5>Description</h5>
  <p class="lead">Evidence-based writing on food, fitness and everyday health.</p>
  <p>Daniel is an exercise and nutrition scientist who turns research into plain language. His work covers proteins, carbohydrates, fats, vitamins and minerals, and the honest facts behind popular supplements. He has published widely on sports performance and healthy ageing.</p>
  <p>Here you will find articles for every age, guides to reading food and supplement labels, and practical steps that help you eat, train and live a little better each day.</p>
  <span class="btn">Read More</span>
</section>

<h2 class="abs section-title">Latest Blog</h2>

<article class="abs post" style="left:100px;top:1650px">
  <h3>Nutrition</h3>
  <div class="meta">Date: <b>November 02, 2014</b> | Author: <b>Daniel</b> | <b>3 Comments</b></div>
  <p>Most people know protein matters, yet few know how much they truly need or when to eat it. In this article we look at what current studies say about daily intake for active adults, older people and growing teens, and why spreading protein across meals may help muscles recover and grow.</p>
  <p>We also compare whole foods with powders and shakes, explain what the numbers on a label really mean, and point out the claims that do not stand up to the evidence.</p>
  <span class="btn">Read More</span>
  <div class="foot"><span>3 Comments</span><span>Like 150</span><span>Share 120</span></div>
</article>
<div class="abs" style="left:580px;top:1640px;width:620px;height:320px">
  <svg width="620" height="320" viewBox="0 0 620 320" role="img" aria-label="Woman about to eat a fresh salad with vegetables around her">
    <defs><linearGradient id="saladTone" x1="0" y1="0" x2="1" y2="1"><stop offset="0" stop-color="#e9efe4"/><stop offset="1" stop-color="#c9d9b8"/></linearGradient></defs>
    <polygon points="120,0 620,0 620,320 0,320" fill="url(#saladTone)"/>
  </svg>
</div>
<div class="abs catbar" style="left:520px;top:1960px;width:680px;background:var(--blue)">
  <span>Nutrition <i></i></span><span>Exercise &amp; Sport <i></i></span><span><i></i></span><span>Sports <i></i></span>
</div>

<div class="abs" style="left:0;top:2060px;width:640px;height:340px">
  <svg width="640" height="340" viewBox="0 0 640 340" role="img" aria-label="Athlete splashing water over her face after a workout">
    <defs><linearGradient id="sportTone" x1="0" y1="0" x2="1" y2="1"><stop offset="0" stop-color="#2a2a2a"/><stop offset="1" stop-color="#6b5546"/></linearGradient></defs>
    <polygon points="0,0 640,0 500,340 0,340" fill="url(#sportTone)"/>
  </svg>
</div>
<div class="abs catbar" style="left:0;top:2350px;width:620px;background:var(--blue)">
  <span>Nutrition <i></i></span><span>Exercise &amp; Sport <i></i></span><span><i></i></span><span>Sports <i></i></span>
</div>
<article class="abs post" style="left:640px;top:2080px;text-align:right">
  <h3>Sports</h3>
  <div class="meta">Date: <b>November 02, 2014</b> | Author: <b>Daniel</b> | <b>3 Comments</b></div>
  <p>Hydration can make or break a training session. Losing even a small share of body water lowers strength, speed and focus, yet drinking too much brings its own risks. Here we explain how to judge your needs before, during and after exercise.</p>
  <p>We look at sports drinks, electrolytes and plain water, and show simple ways to plan fluids for long runs, hot days and team games.</p>
  <span class="btn">Read More</span>
  <div class="foot" style="justify-content:flex-end"><span>3 Comments</span><span>Like 150</span><span>Share 120</span></div>
</article>

<div class="abs panels"></div>
<section class="abs panel" style="left:100px">
  <h3><i></i>Community Feed</h3>
  <ul class="feed">
    <li><div class="avatar" role="img" aria-label="Member photo"></div><div><b>New recipe shared</b><p>Try this quick high protein breakfast bowl today.</p><p>5 minutes ago</p></div></li>
    <li><div class="avatar" role="img" aria-label="Member photo"></div><div><b>Label question</b><p>What does daily value really mean on a pack?</p><p>5 minutes ago</p></div></li>
    <li><div class="avatar" role="img" aria-label="Member photo"></div><div><b>Training log</b><p>First week of strength work done, feeling great.</p><p>5 minutes ago</p></div></li>
  </ul>
</section>
<section class="abs panel" style="left:441px">
  <h3><i></i>Updates Feed</h3>
  <ul class="feed">
    <li><div class="avatar" role="img" aria-label="Reader photo"></div><div><b>Pleasure <small>@fernwell</small></b><p>New article on vitamin D for older adults is live.</p><p>5 minutes ago</p></div></li>
    <li><div class="avatar" role="img" aria-label="Reader photo"></div><div><b>Pleasure <small>@fernwell</small></b><p>Five myths about carbs and weight, explained.</p><p>5 minutes ago</p></div></li>
    <li><div class="avatar" role="img" aria-label="Reader photo"></div><div><b>Sam <small>@fernwell</small></b><p>Join our community forum and ask a question.</p><p>5 minutes ago</p></div></li>
  </ul>
</section>
<section class="abs panel" style="left:782px">
  <h3>Testimonials</h3>
  <div class="testimonial">
    <div class="who"><div class="avatar" role="img" aria-label="Reader portrait"></div><div><b>Oren Castell</b><small>Runner</small><small>Reader since 2013</small></div></div>
    <p>These articles finally made sense of the supplements I was buying. Clear, honest and based on real science, I now read every new post and share them with my running group.</p>
    <div class="arrows"><i></i><i></i></div>
  </div>
</section>

<footer class="abs footer">
  <input type="email" placeholder="Email">
  <span class="btn">Submit</span>
  <div class="social"><i></i><i></i><i></i><i></i><i></i><i></i></div>
</footer>
<div class="abs copy"><span class="l">© 2014 FernwellNotes.com. All rights reserved.</span><span class="r">Privacy Policy | Terms of Use</span></div>

</body>
</html>
```